Red Kettle Pictures BIz Card

This will be a biz card for our independent film company
RED KETTLE PICTURES

we have a logo and i need to figure out how to post it to you!

Here is the info we need on the card:

LOGO

dorinda pratchek (lower case!)
dP@RedKettlePix.example
512-684-2273

Red Kettle Pictures, LLC
www.RedKettlePix.example

stories that matter (tagline)

Target Market(s)

adults in the entertainment industry in USA.
need something creative feeling, a bit funky, not to overt.
something eye catchy that people will be inclined to keep.

ask me any questions you have!

Industry/Entity Type

It Company

Requirements
Must have
• good looking! clean and easy to get the contact info. not too busy.
Nice to have
• love the cards where the design is "continued" on the back side.

perhaps the tag and logo on the back side?!?

open to ideas!
Should not have
• nothing "cartoonish"

```html
<!DOCTYPE html>
<html lang="en">
<head>
<meta charset="utf-8">
<title>Red Kettle Pictures – Business Cards</title>
<link rel="stylesheet" href="https://fonts.googleapis.com/css2?family=Arimo:wght@400;700&family=Dancing+Script:wght@400&display=swap">
<style>
  :root {
    --bg: #e8e5e0;
    --red-light: #ee1c2a;
    --red-dark: #b2102a;
    --black: #0d0d0d;
    --white: #ffffff;
    --ink: #1b1b1b;
    --tag-soft: #f3a3a8;
    --tag-red: #e0301e;
    --shadow: 0 10px 22px rgba(0,0,0,.35);
  }
  * { box-sizing: border-box; margin: 0; padding: 0; }
  html, body { width: 1200px; height: 2498px; overflow: hidden; }
  body { background: var(--bg); font-family: "Arimo", Arial, sans-serif; position: relative; }

  .card {
    position: absolute; left: 104px; width: 1014px; height: 576px;
    overflow: hidden; box-shadow: var(--shadow); background: var(--white);
  }
  .card--front-a { top: 38px; }
  .card--back-a  { top: 661px; }
  .card--front-b { top: 1278px; }
  .card--back-b  { top: 1892px; }

  .red-field { background: linear-gradient(100deg, var(--red-dark) 0%, var(--red-light) 45%, var(--red-dark) 100%); }

  .wordmark { position: absolute; font-weight: 400; white-space: nowrap; letter-spacing: -0.5px; }
  .wordmark--dark { color: var(--ink); }
  .wordmark--light { color: var(--white); }

  .tagline { position: absolute; left: 0; right: 0; text-align: center; font-family: "Dancing Script", cursive; font-size: 46px; }

  .holder-name { position: absolute; color: var(--white); font-weight: 700; font-size: 44px; }
  .contact { position: absolute; color: var(--white); font-size: 27px; line-height: 1; }
  .contact-line { display: flex; align-items: center; gap: 16px; margin-top: 12px; }
  .contact-line svg { width: 20px; height: 20px; fill: var(--white); flex: none; }
  .contact-address { margin-bottom: 38px; }

  .footer-strip { position: absolute; bottom: 0; height: 42px; background: var(--black); color: var(--white); font-size: 22px; display: flex; align-items: center; justify-content: center; }

  /* Front A */
  .card--front-a .top-band { position: absolute; left: 0; top: 0; width: 100%; height: 170px; background: var(--white); }
  .card--front-a .divider { position: absolute; left: 0; top: 170px; width: 100%; height: 14px; background: var(--black); }
  .card--front-a .red-field { position: absolute; left: 0; top: 184px; width: 100%; height: 392px; }
  .card--front-a .wordmark { left: 0; right: 0; top: 68px; text-align: center; font-size: 56px; }
  .card--front-a .holder-name { left: 40px; top: 238px; }
  .card--front-a .contact { left: 560px; top: 372px; }
  .card--front-a .footer-strip { left: 0; width: 100%; }

  /* Back A */
  .card--back-a { }
  .card--back-a .red-field { position: absolute; inset: 0; }
  .card--back-a .wordmark { left: 0; right: 0; top: 240px; text-align: center; font-size: 64px; }
  .card--back-a .tagline { top: 350px; color: var(--tag-soft); }

  /* Front B */
  .card--front-b .red-field { position: absolute; inset: 0; }
  .card--front-b .swoosh { position: absolute; left: 0; top: 0; width: 1014px; height: 576px; }
  .card--front-b .wordmark { left: 20px; top: 268px; font-size: 40px; }
  .card--front-b .holder-name { left: 578px; top: 52px; }
  .card--front-b .contact { left: 580px; top: 205px; }
  .card--front-b .footer-strip { left: 140px; right: 0; }

  /* Back B */
  .card--back-b .wordmark { left: 0; right: 0; top: 232px; text-align: center; font-size: 64px; }
  .card--back-b .tagline { top: 352px; color: var(--tag-red); }
</style>
</head>
<body>

<section class="card card--front-a" aria-label="Business card front, version one">
  <div class="top-band"></div>
  <div class="wordmark wordmark--dark">Red Kettle Pictures</div>
  <div class="divider"></div>
  <div class="red-field"></div>
  <div class="holder-name">dorinda pratchek</div>
  <div class="contact">
    <div class="contact-address">Address</div>
    <div class="contact-line">
      <svg viewBox="0 0 20 20" aria-hidden="true"><path d="M2 7c0-3 3-4 8-4s8 1 8 4v2h-4V7H6v2H2z M5 10h10l2 7H3z"/></svg>
      <span>512-684-2273</span>
    </div>
    <div class="contact-line">
      <svg viewBox="0 0 20 20" aria-hidden="true"><path d="M2 5h16v11H2z M3 6l7 5 7-5v1l-7 5-7-5z" fill-rule="evenodd"/></svg>
      <span>dP@RedKettlePix.example</span>
    </div>
  </div>
  <div class="footer-strip">www.RedKettlePix.example</div>
</section>

<section class="card card--back-a" aria-label="Business card back, version one">
  <div class="red-field"></div>
  <div class="wordmark wordmark--light">Red Kettle Pictures</div>
  <div class="tagline">“stories that matter ”</div>
</section>

<section class="card card--front-b" aria-label="Business card front, version two">
  <div class="red-field"></div>
  <svg class="swoosh" viewBox="0 0 1014 576" aria-hidden="true">
    <path d="M0 0 L30 0 C330 40 500 200 470 576 L0 576 Z" fill="var(--black)"/>
    <path d="M0 30 C300 70 450 230 420 576 L0 576 Z" fill="var(--white)"/>
  </svg>
  <div class="wordmark wordmark--dark">Red Kettle Pictures</div>
  <div class="holder-name">dorinda pratchek</div>
  <div class="contact">
    <div class="contact-address">Address</div>
    <div class="contact-line" style="margin-top:58px">
      <svg viewBox="0 0 20 20" aria-hidden="true"><path d="M2 7c0-3 3-4 8-4s8 1 8 4v2h-4V7H6v2H2z M5 10h10l2 7H3z"/></svg>
      <span>512-684-2273</span>
    </div>
    <div class="contact-line">
      <svg viewBox="0 0 20 20" aria-hidden="true"><path d="M2 5h16v11H2z M3 6l7 5 7-5v1l-7 5-7-5z" fill-rule="evenodd"/></svg>
      <span>dP@RedKettlePix.example</span>
    </div>
  </div>
  <div class="footer-strip">www.RedKettlePix.example</div>
</section>

<section class="card card--back-b" aria-label="Business card back, version two">
  <div class="wordmark wordmark--dark">Red Kettle Pictures</div>
  <div class="tagline">“stories that matter ”</div>
</section>

</body>
</html>
```